A starter web site for the Brisco Tandem Works Association. Our target market are companies that use cyber security products and services and those who provide them.

Target Market(s)

Companies that provide cyber security products and services.

Industry/Entity Type

Security

Coding

Coded - Design and coding required

Number of Pages Required

5+ page

Font styles to use
Serif

Requirements
Must have
• We need the site to have an editor so we can add content, pictures and links to video on Flicora.
Nice to have
• If possible a way to collect names of people interested in joining the organization. that falls into a excel spreadsheet.
Should not have
• Hard to read characters

```html
<!DOCTYPE html>
<html lang="en">
<head>
<meta charset="utf-8">
<title>Brisco Tandem Works Association</title>
<link rel="stylesheet" href="https://fonts.googleapis.com/css2?family=Roboto+Slab:wght@700&family=Roboto+Condensed:wght@400;700&family=Roboto:wght@400;500&display=swap">
<style>
:root{
  --brand:#0b6fbd;
  --nav:#0a70c0;
  --tab:#1390dc;
  --ink:#1d1d1d;
  --muted:#333;
  --panel:#eff1f4;
  --rule:#c9c9c9;
  --footer:#2a292b;
  --dark-btn:#141414;
}
*{box-sizing:border-box;margin:0;padding:0}
html,body{width:1000px;height:1200px;overflow:hidden;background:#fff}
body{position:relative;font-family:"Roboto",Arial,sans-serif;color:var(--ink)}
.abs{position:absolute}

.logo{left:127px;top:9px;font-family:"Roboto Slab",Georgia,serif;font-weight:700;font-size:17px;line-height:21.5px;color:var(--brand);letter-spacing:.3px;text-transform:uppercase}
.call{left:592px;top:24px;display:flex;gap:8px;align-items:flex-start}
.call-text{font-family:"Roboto",Arial,sans-serif;color:var(--brand);line-height:17px}
.call-text .label{font-size:14px;color:#6a7e92}
.call-text .num{font-size:17px;letter-spacing:.6px}
.search{left:778px;top:26px;width:94px;height:28px;border:1px solid #bdbdbd;font-size:9px;color:#777;padding:9px 7px;display:flex;justify-content:space-between}

.nav{left:0;top:82px;width:1000px;height:38px;background:var(--nav);display:flex;padding-left:127px}
.nav a{font-family:"Roboto Condensed",Arial,sans-serif;font-weight:700;font-size:11.5px;color:#fff;text-decoration:none;line-height:38px;padding:0 23px;border-right:1px solid rgba(0,0,0,.18)}
.nav a:first-child{padding-left:0}
.nav a:last-child{border-right:0;padding-right:0}

.hero{left:127px;top:128px;width:745px;height:290px;background:linear-gradient(90deg,#0b1330 0%,#142a66 30%,#0d1a46 55%,#3a2d48 75%,#c46420 92%,#3a3240 100%)}
.hero-arrow{top:120px;width:40px;height:45px;background:rgba(80,80,80,.75)}
.hero-bar{left:143px;top:255px;width:452px;height:20px;background:rgba(20,20,20,.85);border-radius:2px}

.tab{height:26px;background:var(--tab);color:#fff;font-size:13px;letter-spacing:.4px;padding:0 13px;line-height:26px;font-weight:500}
.view-more{left:805px;top:442px;width:67px;height:22px;background:var(--dark-btn);color:#fff;font-size:9px;font-weight:500;text-align:center;line-height:22px}

.card{width:237px}
.card .photo{height:102px;box-shadow:0 6px 6px -3px rgba(0,0,0,.45)}
.card h3{font-family:"Roboto Condensed",Arial,sans-serif;font-weight:700;font-size:11.3px;line-height:14px;margin-top:13px;text-transform:uppercase;color:#111}
.card p{font-size:9px;line-height:11px;margin-top:4px;color:var(--muted);letter-spacing:.15px}
.card .rule{height:2px;background:var(--rule);margin-top:10px}

.panel{top:864px;height:241px;background:var(--panel);overflow:hidden}
.panel .shot{position:absolute;left:0;right:0;bottom:0;height:120px}
.panel .btn{position:absolute;top:189px;height:24px;background:rgba(40,40,40,.85);color:#fff;font-size:9.5px;font-weight:500;line-height:24px;padding:0 6px}
.mission-text{position:absolute;left:23px;top:23px;width:190px;font-size:10px;line-height:17px;color:#222;z-index:1}
.list{position:absolute;list-style:none;font-size:9.8px;line-height:14px;color:#222;z-index:1}
.list li{position:relative;padding-left:12px}
.list li::before{content:"";position:absolute;left:1px;top:4px;border-left:4px solid #222;border-top:3px solid transparent;border-bottom:3px solid transparent}
.date{font-size:8.2px;font-style:italic;font-weight:500;color:var(--tab);padding-left:12px;margin-top:1px}

.footer{left:0;top:1124px;width:1000px;height:76px;background:var(--footer);color:#fff;font-family:"Roboto Condensed",Arial,sans-serif;font-weight:700;font-size:9.5px}
.social{position:absolute;left:128px;top:36px;display:flex;gap:3px}
.social span{width:18px;height:18px;background:#1f6fb2}
.foot-links{position:absolute;right:128px;top:17px;text-align:right;line-height:17px}
</style>
</head>
<body>

<div class="abs logo">Brisco<br>Tandem Works<br>Association</div>

<div class="abs call">
  <svg width="18" height="22" viewBox="0 0 18 22" aria-hidden="true"><path d="M4 1c1.5-.5 2.5 0 3 1.5l1 3.5c.3 1-.3 1.8-1.3 2.3l-1 .5c.7 3 2.4 5.6 4.8 7.4l.9-.7c.9-.6 1.9-.6 2.6.3l2.2 2.6c.9 1 .6 2.1-.4 2.8-1.5 1-3.4 1.4-5.2.6C6 19.3 2.4 13.7 1.6 7.4 1.2 4.7 2 2 4 1z" fill="#8a9097"/></svg>
  <div class="call-text"><div class="label">CALL US</div><div class="num">555.XXX.XXXX</div></div>
</div>

<div class="abs search"><span>SEARCH</span>
  <svg width="10" height="10" viewBox="0 0 10 10" aria-hidden="true"><circle cx="4" cy="4" r="3" fill="none" stroke="#888" stroke-width="1.1"/><path d="M6.3 6.3 9.2 9.2" stroke="#888" stroke-width="1.2"/></svg>
</div>

<nav class="abs nav">
  <a>HOME</a><a>ABOUT US</a><a>MEMBERSHIP FEES AND BENEFITS</a><a>EDUCATION</a><a>EVENTS</a><a>MEDIA</a><a>RESEARCH CENTER</a>
</nav>

<section class="abs hero" role="img" aria-label="Video still: technician working among glowing server racks in a data center">
  <div class="abs hero-arrow" style="left:0">
    <svg width="40" height="45" viewBox="0 0 40 45" aria-hidden="true"><path d="M24 14 16 22.5 24 31" fill="none" stroke="#fff" stroke-width="1.5"/></svg>
  </div>
  <div class="abs hero-arrow" style="right:0">
    <svg width="40" height="45" viewBox="0 0 40 45" aria-hidden="true"><path d="M16 14 24 22.5 16 31" fill="none" stroke="#fff" stroke-width="1.5"/></svg>
  </div>
  <svg class="abs" style="left:347px;top:110px" width="50" height="50" viewBox="0 0 50 50" aria-hidden="true"><circle cx="25" cy="25" r="22" fill="none" stroke="#fff" stroke-width="4"/><path d="M19 14v22l17-11z" fill="#fff"/></svg>
  <div class="abs hero-bar">
    <svg width="452" height="20" viewBox="0 0 452 20" aria-hidden="true">
      <path d="M10 5v10l9-5z" fill="#fff"/>
      <rect x="50" y="8" width="354" height="4" fill="#3a3a3a"/>
      <rect x="50" y="8" width="28" height="4" fill="#777"/>
      <rect x="39" y="-5" width="22" height="9" fill="#111" stroke="#666" stroke-width=".5"/>
      <text x="42" y="2" fill="#fff" font-size="6" font-family="Roboto,Arial,sans-serif">00:03</text>
      <g fill="#d9363e"><rect x="395" y="7" width="1.4" height="6"/><rect x="398" y="7" width="1.4" height="6"/><rect x="401" y="7" width="1.4" height="6"/><rect x="404" y="7" width="1.4" height="6"/><rect x="407" y="7" width="1.4" height="6"/><rect x="410" y="7" width="1.4" height="6"/></g>
      <text x="414" y="14" fill="#d9363e" font-size="9" font-weight="700" font-style="italic" font-family="Roboto,Arial,sans-serif">HD</text>
      <path d="M436 6l3 3M443 6l-3 3M436 14l3-3M443 14l-3-3" stroke="#fff" stroke-width="1.3"/>
    </svg>
  </div>
</section>

<div class="abs tab" style="left:127px;top:438px">OUR PROGRAMME</div>
<div class="abs view-more">VIEW MORE</div>

<article class="abs card" style="left:127px;top:469px">
  <div class="photo" role="img" aria-label="Photo: digital security lock over streams of binary code" style="background:linear-gradient(110deg,#a9c2dc,#2f5c94 45%,#163a6c)"></div>
  <h3>Developing and implementing<br>cyber security plans</h3>
  <p>Contrary to popular belief, Lorem Ipsum is not simply random text</p>
  <div class="rule"></div>
</article>
<article class="abs card" style="left:381px;top:469px">
  <div class="photo" role="img" aria-label="Photo: handshake icon over a blue circuit board pattern" style="background:linear-gradient(120deg,#0a3f86,#1466b8 55%,#0c4a98)"></div>
  <h3>Internal communication strategies<br>and content</h3>
  <p>Contrary to popular belief, Lorem Ipsum is not simply random text</p>
  <div class="rule"></div>
</article>
<article class="abs card" style="left:635px;top:469px">
  <div class="photo" role="img" aria-label="Photo: hand plugging a cable into a laptop port" style="background:linear-gradient(160deg,#e9e9eb,#d9b6a0 50%,#c3c4c8)"></div>
  <h3>External communicationstrategies<br>and content</h3>
  <p>Contrary to popular belief, Lorem Ipsum is not simply random text</p>
  <div class="rule"></div>
</article>

<article class="abs card" style="left:127px;top:659px">
  <div class="photo" role="img" aria-label="Photo: hand touching floating mobile app icons" style="background:radial-gradient(circle at 55% 45%,#7b5a2e,#2a2016 55%,#0d0f14)"></div>
  <h3>New phone apps</h3>
  <p>Contrary to popular belief, Lorem Ipsum is not simply random text</p>
</article>
<article class="abs card" style="left:381px;top:659px">
  <div class="photo" role="img" aria-label="Photo: hands assembling components on a motherboard" style="background:linear-gradient(135deg,#1c3552,#2f6ea0 50%,#0f2238)"></div>
  <h3>New hardware</h3>
  <p>Contrary to popular belief, Lorem Ipsum is not simply random text</p>
</article>
<article class="abs card" style="left:635px;top:659px">
  <div class="photo" role="img" aria-label="Photo: engineer with technical diagrams and a glowing globe" style="background:linear-gradient(100deg,#e2e8ee,#3a8a9a 55%,#1b4e8a)"></div>
  <h3>New software</h3>
  <p>Contrary to popular belief, Lorem Ipsum is not simply random text</p>
</article>

<div class="abs tab" style="left:127px;top:839px;height:25px;line-height:25px;padding:0 10px">OUR MISSION</div>
<section class="abs panel" style="left:127px;width:241px">
  <p class="mission-text">To encourage cyber security professionals to share best practices, obtain knowledge about new products/services and to constantly improve the protection of businesses located in the Commonwealth.</p>
  <div class="shot" role="img" aria-label="Photo: compass dial pointing to the word mission" style="background:linear-gradient(180deg,rgba(239,241,244,0),#d6d8db 45%,#b9bcc1)"></div>
  <div class="btn" style="left:77px">READ MORE</div>
</section>

<div class="abs tab" style="left:380px;top:839px;height:25px;line-height:25px;padding:0 12px">BENEFITS</div>
<section class="abs panel" style="left:379px;width:243px">
  <ul class="list" style="left:17px;top:22px;width:215px">
    <li style="margin-bottom:5px">Product discounts</li>
    <li style="margin-bottom:8px">Research and surveys on issues</li>
    <li style="margin-bottom:10px">Private label cyber security alerts that can be sent to their clients and employees</li>
    <li>Monthly conference call roundtables</li>
  </ul>
  <div class="shot" role="img" aria-label="Photo: raised hands holding colourful letters spelling benefits" style="height:110px;background:linear-gradient(180deg,rgba(239,241,244,0) 0%,#e6a23a 30%,#c8483c 55%,#8a5a3e 100%)"></div>
  <div class="btn" style="left:87px">READ MORE</div>
</section>

<div class="abs tab" style="left:632px;top:839px;height:25px;line-height:25px;padding:0 11px">EVENTS</div>
<section class="abs panel" style="left:632px;width:242px">
  <ul class="list" style="left:16px;top:22px;width:212px;line-height:15.5px">
    <li>There will be different levels of programing and content focused on level of experiences and expertise.</li>
  </ul>
  <div class="abs" style="left:16px;top:82px;z-index:1"><div class="date" style="padding-left:4px">MAY 2014</div></div>
  <div class="abs" style="left:16px;top:88px;width:206px;height:1px;background:#c8c8c8;top:98px;z-index:1"></div>
  <ul class="list" style="left:16px;top:100px;width:212px;line-height:15.5px">
    <li>Programing and content focused on level of experiences and expertise.</li>
  </ul>
  <div class="abs" style="left:16px;top:136px;z-index:1"><div class="date" style="padding-left:12px">JUNE 2014</div></div>
  <div class="shot" role="img" aria-label="Photo: pen resting on a calendar page" style="height:125px;background:linear-gradient(180deg,rgba(239,241,244,0),#d7d9dd 40%,#a9adb4)"></div>
  <div class="btn" style="left:91px">READ MORE</div>
</section>

<footer class="abs footer">
  <div class="abs" style="left:126px;top:17px">CONNECT WITH US</div>
  <div class="social" aria-label="Social links"><span></span><span></span><span></span></div>
  <div class="foot-links">ABOUT US &nbsp;| &nbsp;MEMBERSHIP &nbsp;| &nbsp;EDUCATION &nbsp;| &nbsp;EVENTS &nbsp;| &nbsp;MEDIA &nbsp;| &nbsp;RESEARCH CENTER<br>COPYRIHTS @ 2014 ALL RIGHTS RESERVED</div>
</footer>

</body>
</html>
```